Modern Minimalistic Supplement Label

Opportunity for recurring projects with a growing company. We have provided a detailed creative brief and all necessary files and guidelines. If you have any questions we will be closely monitoring the discussion board and email provided.

THE NAMES LISTED IN THE BRIEF ARE DIFFERENT FROM THE LABEL TEMPLATES. This is a private label brand. The label templates given are generic so please examine the entire brief before starting.

Use the PSD mockups attached and pair the labels with the correct bottles.

Do not use an entirely white background.

This could be excellent portfolio material.

Start by looking at the "CREATIVE_BRIEF" file. Logo files are contained in the "58213907" zip file.

UPDATE* Use the following business address for the "manufactured for" box on the labels.

Fernwick
4817 Larkmoor Ave. #2209
Ann Arbor MI 48196

Target Market(s)

All information provided in "CREATIVE_BRIEF" file.

Industry/Entity Type

Supplement

Requirements
Must have
• All information provided in "CREATIVE_BRIEF" file.
Nice to have
Should not have

```html
<!DOCTYPE html>
<html lang="en">
<head>
<meta charset="utf-8">
<title>Fernwick BCAA 2:1:1 Label</title>
<link href="https://fonts.googleapis.com/css2?family=Arimo:wght@400;700&family=Montserrat:wght@600;700;800&family=Roboto+Condensed:wght@400;700&display=swap" rel="stylesheet">
<style>
  :root {
    --canvas: #e4e4e4;
    --ink: #262425;
    --ink-soft: #2f2c2d;
    --red: #d2232a;
    --red-deep: #b51c22;
    --white: #ffffff;
    --black: #111111;
  }
  * { box-sizing: border-box; margin: 0; padding: 0; }
  html, body { width: 1200px; height: 1097px; overflow: hidden; background: var(--canvas); }
  .label {
    position: absolute; left: 6px; top: 315px; width: 1188px; height: 466px;
    font-family: "Arimo", Arial, sans-serif; color: var(--white);
    background: var(--white);
  }
  .label-shapes { position: absolute; inset: 0; }
  .barcode-zone {
    position: absolute; left: 18px; top: 233px; transform: translate(-50%, -50%) rotate(90deg);
    color: var(--black); font-size: 13px; white-space: nowrap;
  }
  .side-copy {
    position: absolute; left: 50px; top: 13px; width: 309px;
    font-size: 13px; line-height: 15.3px; text-align: justify;
  }
  .side-copy p { margin-bottom: 9px; }
  .side-copy strong { font-weight: 700; }
  .fda-box {
    position: absolute; left: 50px; top: 328px; width: 307px; height: 94px;
    background: var(--white); color: var(--black);
    padding: 9px 14px; font-size: 13px; line-height: 15.2px; text-align: justify; text-transform: uppercase;
    text-indent: 14px;
  }
  .brand-vertical {
    position: absolute; left: 486px; top: 175px; transform: translate(-50%, -50%) rotate(-90deg);
    font-family: "Montserrat", sans-serif; font-weight: 800; font-size: 30px; letter-spacing: 4px;
    color: var(--ink); white-space: nowrap;
  }
  .front-brand {
    position: absolute; left: 579px; top: 80px; width: 200px; text-align: center;
    font-family: "Montserrat", sans-serif; font-weight: 700; font-size: 14px; letter-spacing: 2px;
  }
  .front-brand::before, .front-brand::after {
    content: ""; position: absolute; top: 9px; width: 55px; height: 2px; background: var(--white);
  }
  .front-brand::before { left: -8px; }
  .front-brand::after { right: -8px; }
  .product-name {
    position: absolute; left: 577px; top: 112px; width: 205px; text-align: center;
    font-family: "Montserrat", sans-serif; font-weight: 800; line-height: 1;
  }
  .product-name .line-one { display: block; font-size: 76px; letter-spacing: 1px; }
  .product-name .line-two { display: block; font-size: 86px; margin-top: -2px; }
  .blend-pill {
    position: absolute; left: 577px; top: 293px; width: 203px; height: 26px; border-radius: 13px;
    background: var(--red); text-align: center; line-height: 26px;
    font-family: "Montserrat", sans-serif; font-weight: 600; font-size: 16px; letter-spacing: 1.5px;
  }
  .facts {
    position: absolute; left: 838px; top: 7px; width: 342px; height: 245px;
    background: var(--white); color: var(--black); padding: 6px 9px 0 9px;
    font-size: 9.5px; line-height: 1.2;
  }
  .facts-title {
    font-family: "Montserrat", sans-serif; font-weight: 800; font-size: 26px; letter-spacing: 0.6px;
    line-height: 30px; margin-bottom: 8px; white-space: nowrap;
  }
  .facts-serving { font-size: 10px; line-height: 13.5px; }
  .rule-thick { height: 4px; background: var(--black); margin: 5px 0 2px; }
  .rule-mid { height: 3px; background: var(--black); margin: 1px 0 2px; }
  .facts-row { display: flex; height: 15px; align-items: center; border-bottom: 1px solid var(--black); }
  .facts-row.no-line { border-bottom: none; }
  .facts-row .name { flex: 1; }
  .facts-row .amount { width: 60px; text-align: right; }
  .facts-row .dv { width: 50px; text-align: right; padding-right: 4px; }
  .facts-row.head { font-weight: 700; }
  .facts-row.indent .name { padding-left: 10px; }
  .facts-note { font-size: 8px; line-height: 10.5px; margin-top: 4px; }
  .front-copy {
    position: absolute; left: 837px; width: 345px; font-size: 11.6px; line-height: 15px; text-align: justify;
  }
  .front-copy.ingredients { top: 259px; }
  .front-copy.allergen { top: 311px; }
  .claim {
    position: absolute; left: 550px; top: 400px;
    font-family: "Montserrat", sans-serif; font-weight: 600; font-size: 14px; letter-spacing: 1.4px;
  }
  .net-weight {
    position: absolute; left: 563px; top: 434px;
    font-family: "Roboto Condensed", sans-serif; font-weight: 700; font-size: 10.5px; letter-spacing: 1px;
  }
  .maker {
    position: absolute; left: 977px; top: 390px; font-family: "Roboto Condensed", sans-serif; font-size: 11px; line-height: 13px;
  }
  .maker .heading { font-family: "Arimo", sans-serif; font-size: 12px; margin-bottom: 10px; }
  .maker .company { font-weight: 700; font-size: 12px; }
</style>
</head>
<body>
<div class="label">
  <svg class="label-shapes" width="1188" height="466" viewBox="0 0 1188 466">
    <rect width="1188" height="466" fill="var(--white)"/>
    <path d="M42 0 H345 Q411 0 411 60 V406 Q411 466 345 466 H42 Z" fill="var(--red)"/>
    <path d="M42 0 H340 Q402 0 402 62 V404 Q402 466 340 466 H42 Z" fill="var(--ink)"/>
    <path d="M522 48 Q522 0 570 0 H1188 V466 H570 Q522 466 522 418 Z" fill="var(--ink)"/>
    <path d="M522 367 H1188 V466 H570 Q522 466 522 418 Z" fill="var(--red)"/>
    <rect x="609" y="368" width="579" height="6" rx="3" fill="var(--white)"/>
    <g fill="var(--white)" stroke="var(--red)" stroke-width="4">
      <circle cx="467" cy="318" r="22"/>
      <circle cx="467" cy="374" r="22"/>
      <circle cx="467" cy="430" r="22"/>
    </g>
    <g fill="none" stroke="var(--white)" stroke-width="2">
      <circle cx="1129" cy="410" r="8"/>
      <circle cx="1167" cy="410" r="8"/>
      <rect x="1120" y="434" width="18" height="14" rx="2"/>
      <circle cx="1167" cy="441" r="9"/>
    </g>
  </svg>

  <div class="barcode-zone">Bar-Code Zone</div>

  <div class="side-copy">
    <p><strong>Directions:</strong> As a dietary supplement, mix one serving (one level scoop) with 8oz of water. Stir or shake and consume on training days, or throughout the day on both training and non training days.</p>
    <p><strong>WARNING</strong> This product is only intended for healthy adults, 18 years of age or older. Do not use if pregnant or nursing. Consult with a licensed, qualified, healthcare professional before taking this or any dietary supplement product, especially if you are taking medication or have a medical condition. Discontinue 2 weeks prior to surgery. Use only as directed. Do not use if safety seal is broken or missing. Store in a cool, dry place. KEEP OUT OF REACH OF CHILDREN.</p>
    <p>This product is sold by weight not volume. Some settling of powder may occur during shipping and handling, which may affect density of powder.</p>
  </div>
  <div class="fda-box">These statements have not been evaluated by the Food and Drug Administration. These products are not intended to diagnose, treat, cure or prevent any disease.</div>

  <div class="brand-vertical">FERNWICK</div>

  <div class="front-brand">FERNWICK</div>
  <h1 class="product-name"><span class="line-one">BCAA</span><span class="line-two">2:1:1</span></h1>
  <div class="blend-pill">ANABOLIC BLEND</div>

  <div class="facts">
    <div class="facts-title">SUPPLEMENT FACTS</div>
    <div class="facts-serving">SERVING SIZE: 1 SCOOP (7g)<br>SERVINGS PER CONTAINER: 30</div>
    <div class="rule-thick"></div>
    <div class="facts-row head no-line"><span class="name"></span><span class="amount" style="width:130px">Amount Per Serving</span><span class="dv">%DV</span></div>
    <div class="rule-mid"></div>
    <div class="facts-row"><span class="name">Calories</span><span class="amount">0</span><span class="dv"></span></div>
    <div class="facts-row"><span class="name">Carbohydrates</span><span class="amount">0g</span><span class="dv">0%*</span></div>
    <div class="facts-row indent no-line"><span class="name">Sugars</span><span class="amount">0g</span><span class="dv">**</span></div>
    <div class="rule-mid"></div>
    <div class="facts-row"><span class="name">BCAA 2:1:1 FORMULA</span><span class="amount">5g</span><span class="dv"></span></div>
    <div class="facts-row"><span class="name">L-Leucine (instantized, Ultra-Soluble)</span><span class="amount">2500mg</span><span class="dv">**</span></div>
    <div class="facts-row"><span class="name">L-Valine (instantized, Ultra-Soluble)</span><span class="amount">1250mg</span><span class="dv">**</span></div>
    <div class="facts-row no-line"><span class="name">L-Isoleucine (instantized, Ultra-Soluble)</span><span class="amount">1250mg</span><span class="dv">**</span></div>
    <div class="rule-mid"></div>
    <div class="facts-note">*The % Daily Values are based on a 2,000 calorie diet.<br>**% Daily Value not established</div>
  </div>

  <p class="front-copy ingredients">Other Ingredients: Citric Acid, Natural and Artificial Flavors, Sucralose, Silicon Dioxide, Acesulfame Potassium (Ace-K), Maltodextrin.</p>
  <p class="front-copy allergen">Allergen Warning: This product is manufacterd with equip,emt that process products that may contain milk, egg, soy, tree nuts, peanuts, wheat, fish, crustaceans &amp; shellfish.</p>

  <div class="claim">FOR INCREASED PROTEIN SYNTHESIS</div>
  <div class="net-weight">NET WT.&nbsp; 210 G (7.41 OZ) &nbsp;|&nbsp; DIETARY SUPPLEMENT</div>

  <div class="maker">
    <div class="heading">Manufactured for:</div>
    <div class="company">Fernwick</div>
    <div>4817 Larkmoor Ave. #2209</div>
    <div>Ann Arbor MI 48196</div>
  </div>
</div>
</body>
</html>
```